Business Card Design

Hoping for a black background business card, minimalistic design.
With the Marble Crest logo you created in white.

I would like to include:
My Name and title
Address (street address)
Reception: (phone number)
Fax: (fax number)
Reception: (email address)
Direct email: (email address)
Instagram: (ig handle)

```html
<!DOCTYPE html>
<html lang="en">
<head>
<meta charset="utf-8">
<title>Marble Crest Business Card</title>
<link rel="stylesheet" href="https://fonts.googleapis.com/css2?family=Montserrat:wght@400;500;700&family=Lato:wght@400;700&display=swap">
<style>
  :root {
    --backdrop: #2c2e31;
    --card-dark: #1d1e20;
    --white: #ffffff;
    --text-soft: #c9cacc;
    --ring-faint: #2b2c2f;
  }
  * { margin: 0; padding: 0; box-sizing: border-box; }
  html, body {
    width: 1200px; height: 952px; overflow: hidden;
    background: var(--backdrop);
  }
  .canvas {
    position: relative; width: 1200px; height: 952px;
    display: flex; align-items: center; justify-content: center; gap: 60px;
  }
  .card {
    width: 520px; height: 297px; border-radius: 22px;
    position: relative; overflow: hidden;
    background: var(--card-dark);
    box-shadow: 0 18px 40px rgba(0,0,0,0.45);
  }

  /* Front: wordmark */
  .brand {
    position: absolute; inset: 0;
    display: flex; align-items: center; justify-content: center; gap: 20px;
  }
  .brand__ring {
    width: 62px; height: 62px; border-radius: 50%;
    border: 3px solid var(--white);
  }
  .brand__divider {
    width: 1.5px; height: 74px; background: var(--white);
    transform: rotate(12deg);
  }
  .brand__name {
    font-family: "Montserrat", sans-serif; font-weight: 500;
    font-size: 30px; letter-spacing: 3px; color: var(--white);
    text-transform: uppercase;
  }

  /* Back: contact details */
  .person { position: absolute; left: 36px; top: 26px; }
  .person__name {
    font-family: "Montserrat", sans-serif; font-size: 18px;
    font-weight: 500; color: var(--white); letter-spacing: 0.5px;
    text-transform: uppercase;
  }
  .person__name strong { font-weight: 700; }
  .person__title {
    font-family: "Lato", sans-serif; font-size: 13px; color: var(--text-soft);
    margin-top: 2px;
  }
  .person__rule { width: 52px; height: 2px; background: var(--white); margin-top: 7px; }

  .contact { position: absolute; left: 36px; top: 104px; list-style: none; }
  .contact__item {
    display: flex; align-items: flex-start; gap: 8px;
    font-family: "Lato", sans-serif; font-size: 11px; line-height: 1.3;
    color: var(--text-soft); margin-bottom: 5px;
  }
  .contact__label { color: var(--white); font-weight: 700; }
  .contact__icon {
    width: 14px; height: 14px; border-radius: 2px; background: var(--white);
    flex: none; display: flex; align-items: center; justify-content: center;
  }
  .contact__icon svg { width: 10px; height: 10px; }

  .emblem {
    position: absolute; right: 26px; top: 70px;
    width: 200px; height: 200px; border-radius: 50%;
    border: 12px solid var(--ring-faint);
    display: flex; align-items: center; justify-content: center;
  }
  .emblem__name {
    font-family: "Montserrat", sans-serif; font-weight: 700;
    font-size: 22px; letter-spacing: 2px; color: var(--white);
    text-transform: uppercase; text-align: center; line-height: 1.15;
  }
</style>
</head>
<body>
<main class="canvas">
  <section class="card card--front" aria-label="Card front">
    <div class="brand">
      <span class="brand__ring"></span>
      <span class="brand__divider"></span>
      <span class="brand__name">Marble Crest</span>
    </div>
  </section>

  <section class="card card--back" aria-label="Card back">
    <div class="emblem"><span class="emblem__name">Marble<br>Crest</span></div>

    <header class="person">
      <h1 class="person__name">Daniel R. <strong>Whitmore</strong></h1>
      <p class="person__title">Managing Director</p>
      <div class="person__rule"></div>
    </header>

    <ul class="contact">
      <li class="contact__item">
        <span class="contact__icon"><svg viewBox="0 0 10 10"><path d="M5 1a3 3 0 0 0-3 3c0 2.2 3 5 3 5s3-2.8 3-5a3 3 0 0 0-3-3zm0 4.2a1.2 1.2 0 1 1 0-2.4 1.2 1.2 0 0 1 0 2.4z" fill="#1d1e20"/></svg></span>
        <span>2710 Harbor Lane<br>Portland, OR 97205</span>
      </li>
      <li class="contact__item">
        <span class="contact__icon"><svg viewBox="0 0 10 10"><path d="M2.5 1l1.5 2-1 1c.5 1.2 1.3 2 2.5 2.5l1-1 2 1.5-1 1.5C4.5 9 1 5.5 1 2z" fill="#1d1e20"/></svg></span>
        <span><span class="contact__label">Reception:</span> +00 987 654 32</span>
      </li>
      <li class="contact__item">
        <span class="contact__icon"><svg viewBox="0 0 10 10"><rect x="3" y="1" width="4" height="3" fill="none" stroke="#1d1e20" stroke-width="0.9"/><rect x="1" y="4" width="8" height="3.5" fill="#1d1e20"/><rect x="3" y="6.5" width="4" height="2.5" fill="none" stroke="#1d1e20" stroke-width="0.9"/></svg></span>
        <span><span class="contact__label">Fax:</span> +00 987 654 33</span>
      </li>
      <li class="contact__item">
        <span class="contact__icon"><svg viewBox="0 0 10 10"><rect x="1" y="2.5" width="8" height="5" fill="none" stroke="#1d1e20" stroke-width="1"/><path d="M1 2.5l4 3 4-3" fill="none" stroke="#1d1e20" stroke-width="1"/></svg></span>
        <span><span class="contact__label">Reception:</span> office@marblecrestmail.com</span>
      </li>
      <li class="contact__item">
        <span class="contact__icon"><svg viewBox="0 0 10 10"><rect x="1" y="2.5" width="8" height="5" fill="none" stroke="#1d1e20" stroke-width="1"/><path d="M1 2.5l4 3 4-3" fill="none" stroke="#1d1e20" stroke-width="1"/></svg></span>
        <span><span class="contact__label">Direct:</span> daniel@marblecrestmail.com</span>
      </li>
      <li class="contact__item">
        <span class="contact__icon"><svg viewBox="0 0 10 10"><circle cx="5" cy="5" r="2.6" fill="#1d1e20"/></svg></span>
        <span><span class="contact__label">Instagram:</span> @marblecrest.studio</span>
      </li>
    </ul>
  </section>
</main>
</body>
</html>
```